Eye Doctor Website

We are looking for a new logo and update to our website.

The Practice Name is Dr. Lydia Pennholt and Associates

This is a simple straight forward project that requires some aspect of Optometry or eye care in the logo. Also we are located in Colorado so if we are open to the idea of adding some element of the Colorado state flag or image of the mountains

For the web all the text is already complete visit www.drlydiapennholt.example to see what we currently have we will be taking what you created and updating this site.

We would like the new logo to be used on the web and on business cards.

Please only submit the first page of the web site. Then we can get the rest from there.

Text does not need to be included for the design but would help.

Good luck and let us know if you have any questions

Target Market(s)

30-50 year olds looking for an eye exam.

Site must be fun but also serious and professional to catch the patients attention. Trying to play on outdoor theme

Font styles to use
Serif

Colors

Designer to choose colors to be used in the design.

Requirements
Must have
• Need a theme to play off of... Either use the state flag of Colorado or something with mountains. We are very close to the Halvern Peaks so this would work.

Want this them to play throughout the whole site and on Business cards
Nice to have
• Simple navigation. Don't need a lot of text
Should not have
• Clutter.... Simple to the point.

```html
<!DOCTYPE html>
<html lang="en">
<head>
<meta charset="utf-8">
<title>Dr. Lydia Pennholt and Associates</title>
<link rel="stylesheet" href="https://fonts.googleapis.com/css2?family=Cinzel:wght@700&family=Open+Sans:wght@400;600&family=Oxygen:wght@400;700&display=swap">
<style>
:root{
  --blue:#0a9ad8;
  --blue-light:#13b3ee;
  --blue-dark:#0580bd;
  --text:#555;
  --text-dark:#444;
  --grey-bar:#e6e6e6;
  --grey-line:#d4d4d4;
  --panel:#f0f0f0;
  --footer:#3c3c3c;
  --white:#fff;
}
*{box-sizing:border-box;margin:0;padding:0}
html,body{width:825px;height:1200px;overflow:hidden}
body{position:relative;font-family:"Open Sans",Arial,sans-serif;color:var(--text);background:#fff}
.backdrop{position:absolute;inset:0;background:linear-gradient(180deg,#8fb7dc 0%,#c9dcec 14%,#eef3f7 24%,#6c7f94 42%,#2e3d34 62%,#3c4a40 80%,#e6edf2 100%)}
.page{position:absolute;left:113px;top:0;width:583px;height:890px;background:var(--white)}
.abs{position:absolute}
.brand{left:23px;top:38px;display:flex;align-items:center;gap:14px}
.brand-mark{width:56px;height:56px;border-radius:50%;background:var(--blue)}
.brand-name{font-family:"Cinzel",Georgia,serif;font-weight:700;font-size:17px;line-height:25px;color:var(--blue);letter-spacing:.3px}
.call{right:46px;top:23px;text-align:right;white-space:nowrap}
.call-label{font-size:11.5px;color:var(--text-dark)}
.call-number{font-size:14px;color:var(--blue);margin-top:1px}
.call-icon{position:absolute;right:-23px;top:6px}
.search{left:412px;top:70px;width:150px;height:21px;border:1px solid var(--grey-line);font-size:9px;color:#777;padding:5px 8px}
.search svg{position:absolute;right:6px;top:5px}
.nav{left:12px;top:107px;width:556px;height:33px;background:linear-gradient(var(--blue-light),var(--blue));display:flex}
.nav a{font-family:"Oxygen",Arial,sans-serif;font-size:9.8px;color:#fff;text-decoration:none;display:flex;align-items:center;justify-content:center;white-space:nowrap;border-right:1px solid rgba(255,255,255,.3);height:100%;flex:none}
.nav a.current{background:var(--blue-dark)}
.hero{left:12px;top:141px;width:556px;height:220px;background:linear-gradient(90deg,#e9eef3 0%,#d9e0e6 35%,#c79c83 60%,#8a5a45 100%)}
.hero-copy{left:18px;top:70px;font-size:17px;line-height:27px;color:#4a4a4a}
.dots{left:19px;top:195px;display:flex;gap:5px}
.dots span{width:10px;height:10px;border-radius:50%;background:#bbb}
.dots span.on{background:var(--blue)}
.tile{top:392px;width:165px;height:108px;border:1px solid var(--grey-line);padding:3px;background:#fff}
.tile-image{position:relative;width:100%;height:100%}
.tile-caption{position:absolute;left:0;right:0;bottom:0;height:21px;background:rgba(120,120,120,.6);color:#fff;font-family:"Oxygen",Arial,sans-serif;font-weight:700;font-size:10px;padding:5px 12px}
h2.section{font-family:"Oxygen",Arial,sans-serif;font-weight:400;font-size:16px;color:var(--blue)}
.portrait{left:12px;top:573px;width:113px;height:93px;background:linear-gradient(#7fc6d4,#d8b894)}
.intro{left:146px;top:570px;width:197px;font-size:8.3px;line-height:15px;color:var(--text)}
.service{left:12px;width:352px;height:28px;background:var(--grey-bar);border-radius:2px;display:flex;align-items:center;font-size:9px;color:var(--text-dark);white-space:nowrap}
.service i{width:16px;height:16px;border-radius:50%;background:#fff;margin:0 12px 0 8px;position:relative;flex:none}
.service i::before,.service i::after{content:"";position:absolute;background:#888;left:4px;top:7.5px;width:8px;height:1px}
.service i::after{transform:rotate(90deg)}
.service.open{background:var(--blue);color:#fff;font-size:9.5px}
.service.open i::before,.service.open i::after{background:var(--blue)}
.booking{left:376px;top:538px;width:192px;height:315px;background:var(--panel);border:1px solid #e2e2e2}
.booking-head{height:64px;background:linear-gradient(var(--blue-light),var(--blue));color:#fff;text-align:center;font-family:"Oxygen",Arial,sans-serif;padding-top:11px}
.booking-head h3{font-weight:400;font-size:14.5px}
.booking-head p{font-size:13px;margin-top:5px;display:flex;justify-content:center;align-items:center;gap:8px}
.field{position:absolute;left:10px;width:174px;height:25px;background:#fff;border:1px solid var(--grey-line);font-size:8.5px;color:#666;padding:6px 9px}
.submit{position:absolute;left:32px;top:282px;width:132px;height:28px;background:#8a8d90;color:#fff;font-size:11.5px;display:flex;align-items:center;justify-content:center;border-bottom:2px solid #6f7275}
.map{left:113px;top:890px;width:583px;height:166px;background:linear-gradient(120deg,#e8e4da 0%,#e9e5dc 40%,#a9c7e6 55%,#e8e4da 70%,#f1d88c 100%)}
.footer{left:113px;top:1056px;width:583px;height:144px;background:var(--footer);color:#fff}
.footer h4{font-family:"Oxygen",Arial,sans-serif;font-weight:400;font-size:10px;margin-bottom:10px}
.hours{left:23px;top:32px;font-size:8.3px;line-height:15.3px;white-space:nowrap}
.contact{left:231px;top:32px;font-size:8.3px;white-space:nowrap}
.contact-row{display:flex;gap:9px;align-items:flex-start;line-height:14.5px;margin-bottom:6px}
.contact-row svg{flex:none;margin-top:2px}
.social{left:393px;top:47px;display:flex;gap:8px}
.social span{width:21px;height:21px;background:#6a6e72}
.legal{left:363px;top:82px;width:200px;text-align:center;font-size:8px;line-height:19px;white-space:nowrap}
</style>
</head>
<body>
<div class="backdrop" role="img" aria-label="Snowy mountain slopes with pine forest under a blue sky"></div>

<div class="page">
  <header>
    <div class="abs brand">
      <span class="brand-mark"></span>
      <div class="brand-name">Dr. Lydia Pennholt<br>and Associates</div>
    </div>
    <div class="abs call">
      <div class="call-label">Call today</div>
      <div class="call-number">+61 02 5550 1234</div>
      <svg class="call-icon" width="16" height="20" viewBox="0 0 16 20"><path d="M3 1l3 0 2 5-2 2c1 3 3 5 5 6l2-2 3 2v3c0 1-1 2-2 2C7 18 1 11 1 3c0-1 1-2 2-2z" fill="#0a9ad8"/></svg>
    </div>
    <div class="abs search">Search..
      <svg width="9" height="9" viewBox="0 0 9 9"><circle cx="3.7" cy="3.7" r="2.8" fill="none" stroke="#888" stroke-width="1.2"/><path d="M5.8 5.8L8.5 8.5" stroke="#888" stroke-width="1.3"/></svg>
    </div>
    <nav class="abs nav">
      <a class="current" style="width:65px">HOME</a>
      <a style="width:101px">DR. PENNHOLT</a>
      <a style="width:160px">SCHEDULE AN APPOINTMENT</a>
      <a style="width:132px">OFFICE INFO/SPECIALS</a>
      <a style="width:98px;border-right:0">CONTACT US</a>
    </nav>
  </header>

  <section class="abs hero" role="img" aria-label="Woman placing a contact lens in her eye">
    <p class="abs hero-copy">Lorem ipsum dolor<br>sit amet consectetur<br>adipiscing elit.</p>
    <div class="abs dots"><span class="on"></span><span></span><span></span><span></span></div>
  </section>

  <div class="abs tile" style="left:11px"><div class="tile-image" role="img" aria-label="Patient having an eye exam at a slit lamp" style="background:linear-gradient(90deg,#e4e4e4,#9a9a9a 60%,#c68a68)"><div class="tile-caption">LOREM IPSUM DOLOR</div></div></div>
  <div class="abs tile" style="left:206px"><div class="tile-image" role="img" aria-label="Woman in glasses in front of an eye chart" style="background:linear-gradient(90deg,#e8e8e8,#d6c3b6 50%,#5a3a2c)"><div class="tile-caption">LOREM IPSUM DOLOR</div></div></div>
  <div class="abs tile" style="left:403px"><div class="tile-image" role="img" aria-label="Woman holding a pair of eyeglasses" style="background:linear-gradient(90deg,#f1d9c3,#d9a985 50%,#7a5a4a)"><div class="tile-caption">LOREM IPSUM DOLOR</div></div></div>

  <h2 class="abs section" style="left:12px;top:536px">Welcome to Our Website</h2>
  <div class="abs portrait" role="img" aria-label="Portrait of a smiling staff member"></div>
  <p class="abs intro">Welcome to Dr. Lydia Pennholt's optometry office. We are conveniently located in Brightway at Aspen Grove Center in Larkfield, CO. We are here to provide you and your family with affordable, thorough eye care. Our office employs the latest in eye care technology in order to provide a superior quality of care.</p>

  <h2 class="abs section" style="left:12px;top:688px">Services</h2>
  <div class="abs service open" style="top:722px"><i></i>Comprehensive eye exams with testing for glaucoma, cataracts.</div>
  <div class="abs service" style="top:755px"><i></i>Contact lens exams, including astigmatism (toric), bifocal and gas lenses.</div>
  <div class="abs service" style="top:789px"><i></i>Treatment of eye infections, dry eyes, and other eye problems</div>
  <div class="abs service" style="top:823px"><i></i>Diabetic eye exams</div>

  <aside class="abs booking">
    <div class="booking-head">
      <h3>Make an Appointment</h3>
      <p><svg width="15" height="13" viewBox="0 0 15 13"><path d="M1 4c0-2 3-3 6.5-3S14 2 14 4v1h-3V3.5H4V5H1z" fill="#fff"/><path d="M3 6h9l1.5 6h-12z" fill="#fff"/><circle cx="7.5" cy="8.8" r="1.8" fill="#0a9ad8"/></svg>1-800-555-0147</p>
    </div>
    <div class="field" style="top:85px">Name</div>
    <div class="field" style="top:124px">Phone</div>
    <div class="field" style="top:160px">E-mail</div>
    <div class="field" style="top:197px;height:69px">Message</div>
    <div class="submit">Submit Request</div>
  </aside>
</div>

<div class="abs map" role="img" aria-label="Street map showing the office location"></div>

<footer class="abs footer">
  <div class="abs hours">
    <h4>Working Hours</h4>
    Monday - 10:00am - 6:00pm<br>
    Wednesday - 10:00am - 7:00pm<br>
    Friday - 10:00am - 6:00pm<br>
    Saturday - 9:00am - 5:00pm<br>
    Sunday - 1:00pm - 4:00pm (every other week)
  </div>
  <div class="abs contact">
    <h4>Contact</h4>
    <div class="contact-row"><svg width="8" height="11" viewBox="0 0 8 11"><path d="M4 0a4 4 0 014 4c0 3-4 7-4 7S0 7 0 4a4 4 0 014-4z" fill="#bbb"/><circle cx="4" cy="4" r="1.5" fill="#3c3c3c"/></svg><span>1000 Juniper Ridge Ave.<br>Larkfield CO 80230</span></div>
    <div class="contact-row"><svg width="11" height="8" viewBox="0 0 11 8"><rect x=".5" y=".5" width="10" height="7" fill="none" stroke="#bbb"/><path d="M.5.5l5 4 5-4" fill="none" stroke="#bbb"/></svg><span>info@pennholteyes.example</span></div>
    <div class="contact-row"><svg width="10" height="10" viewBox="0 0 16 20"><path d="M3 1l3 0 2 5-2 2c1 3 3 5 5 6l2-2 3 2v3c0 1-1 2-2 2C7 18 1 11 1 3c0-1 1-2 2-2z" fill="#bbb"/></svg><span>89 555 0198</span></div>
  </div>
  <div class="abs social"><span></span><span></span><span></span><span></span><span></span></div>
  <div class="abs legal">Terms and Conditions | Privacy Policy | Site Map<br>© 2013 Copyrights. All Rights Reserved.</div>
</footer>
</body>
</html>
```